LH Business Card NEEDED

Lumen Harbour is a finance brokering company that provide lending advise to consumer, business, corporate, and property developer for all their financing needs.

We source and match customer needs in Home Loan, Business Loan, Commercial Property Loan, Assets Finance, and other banking related services. It is a market with full of loans! But we specialise in more complex loan structure and our client base are more business and corporate level. Our suppliers are Banks and large Financial Institution where these business card will go to.

We have a great deal of Asian clients, therefore the card need to also include Chinese language together with English.

Refer to attached file for logo and content requirements.

We are looking for designs with the following ingredients:
* Innovative & Creative
* Professional
* Trust & Security

Please pick colours that will compliment the colours of the company logo.

Please provide a unique design, for example the edge of the card is rounded or corner cut off.
Updates

Company logo uploaded.

Please commence submitting your design.

Target Market(s)

Target audiences are businessmen, corporate, and property developer. And also a great deal of Chinese clients.

Industry/Entity Type

Finance

Contact Information for Business Card

Lumen Harbour Pty. Ltd.
Morris Okafor
Director
Suite 42, 7-9 Pellow St. Dunmore NSW 2738

Requirements
Must have
• Double sided design

```html
<!DOCTYPE html>
<html lang="en">
<head>
<meta charset="utf-8">
<title>Lumen Harbour – Business Card</title>
<link rel="stylesheet" href="https://fonts.googleapis.com/css2?family=Arimo:wght@400;700&family=Archivo+Narrow:wght@400&family=Noto+Sans+SC:wght@400;700&display=swap">
<style>
  :root {
    --stage: #dedede;
    --card: #ffffff;
    --red: #d42420;
    --red-deep: #b01e1c;
    --gold: #f0c419;
    --ink: #222222;
    --label: #2a2a2a;
    --corner: 16px;
  }
  * { margin: 0; padding: 0; box-sizing: border-box; }
  html, body { width: 1200px; height: 938px; overflow: hidden; }
  body {
    position: relative;
    background: var(--stage);
    font-family: "Arimo", Arial, sans-serif;
    color: var(--ink);
  }
  .zh { font-family: "Noto Sans SC", "Arimo", sans-serif; }

  .view-label {
    position: absolute;
    font-size: 19px;
    letter-spacing: 0.5px;
    color: var(--label);
  }
  .view-label--front { left: 234px; top: 486px; }
  .view-label--back { left: 870px; top: 430px; }

  .card {
    position: absolute;
    width: 388px;
    height: 237px;
    background: var(--card);
    overflow: hidden;
    border-radius: var(--corner) 0 var(--corner) 0;
  }
  .card--front { left: 191px; top: 218px; }
  .card--back { left: 637px; top: 463px; }
  .card__band { position: absolute; left: 0; top: 0; }

  .brand {
    position: absolute;
    left: 38px;
    top: 110px;
    display: grid;
    grid-template-columns: 10px auto;
    column-gap: 6px;
    row-gap: 2px;
    align-items: center;
    font-size: 11px;
    line-height: 13px;
    color: var(--ink);
  }
  .brand__dot {
    width: 10px; height: 10px; border-radius: 50%;
    background: var(--red);
  }
  .brand__zh { grid-column: 2; font-size: 10px; line-height: 13px; letter-spacing: 1px; }

  .holder {
    position: absolute;
    left: 219px;
    top: 56px;
    width: 126px;
    text-align: center;
  }
  .holder__name {
    font-family: "Archivo Narrow", "Arial Narrow", sans-serif;
    font-size: 19px;
    line-height: 22px;
    white-space: nowrap;
  }
  .holder__rule {
    height: 2px;
    margin-top: 2px;
    background: linear-gradient(to right, var(--red) 0 55%, var(--gold) 55% 100%);
  }
  .holder__title { font-size: 14px; line-height: 18px; margin-top: 3px; }
  .holder__title .zh { font-size: 12px; margin-left: 4px; }

  .office {
    position: absolute;
    left: 230px;
    top: 172px;
    color: #fff;
    font-size: 13px;
    line-height: 17px;
    font-style: normal;
  }
  .office__label { font-weight: 700; font-size: 15px; line-height: 18px; }
  .office__label .zh { font-size: 12px; font-weight: 400; }

  .services {
    position: absolute;
    top: 32px;
    right: 44px;
    display: flex;
    gap: 8px;
  }
  .service {
    width: 62px;
    text-align: center;
    font-size: 10px;
    line-height: 12px;
  }
  .service svg { display: block; margin: 0 auto 8px; }
  .service strong { display: block; font-weight: 700; }
  .service .zh { display: block; margin-top: 2px; font-size: 9px; line-height: 12px; color: var(--red-deep); }
</style>
</head>
<body>
  <p class="view-label view-label--back">BACK VIEW</p>
  <p class="view-label view-label--front">FORWARD VIEW</p>

  <section class="card card--front" aria-label="Front of card">
    <svg class="card__band" width="388" height="237" viewBox="0 0 388 237">
      <defs>
        <linearGradient id="bandFront" x1="0" y1="0" x2="1" y2="0">
          <stop offset="0" stop-color="#c7201d"/>
          <stop offset="0.5" stop-color="#dc2a22"/>
          <stop offset="1" stop-color="#b01e1c"/>
        </linearGradient>
      </defs>
      <path d="M0,222 Q150,150 388,128 L388,237 L0,237 Z" fill="url(#bandFront)"/>
    </svg>
    <div class="brand">
      <span class="brand__dot"></span><span>Lumen Harbour Pty. Ltd.</span>
      <span class="brand__zh zh" lang="zh">朗港金融有限公司</span>
    </div>
    <div class="holder">
      <p class="holder__name">MORRIS OKAFOR</p>
      <div class="holder__rule"></div>
      <p class="holder__title">Director<span class="zh" lang="zh">董事</span></p>
    </div>
    <address class="office">
      <p class="office__label">office <span class="zh" lang="zh">办公室</span> :</p>
      <p>Suite 42, 7-9 Pellow St.</p>
      <p>Dunmore NSW 2738</p>
    </address>
  </section>

  <section class="card card--back" aria-label="Back of card">
    <svg class="card__band" width="388" height="237" viewBox="0 0 388 237">
      <defs>
        <linearGradient id="bandBack" x1="0" y1="0" x2="1" y2="0">
          <stop offset="0" stop-color="#b81f1c"/>
          <stop offset="0.55" stop-color="#dc2a22"/>
          <stop offset="1" stop-color="#b01e1c"/>
        </linearGradient>
      </defs>
      <path d="M0,128 Q120,116 222,158 Q300,192 388,222 L388,237 L0,237 Z" fill="url(#bandBack)"/>
    </svg>
    <div class="services">
      <div class="service">
        <svg width="36" height="36" viewBox="0 0 36 36" aria-hidden="true">
          <circle cx="18" cy="10" r="8" fill="var(--red)"/>
          <path d="M4,36 Q4,20 18,20 Q32,20 32,36 Z" fill="var(--red)"/>
          <path d="M16,20 L20,20 L19,30 L17,30 Z" fill="#fff"/>
        </svg>
        financing<strong>Consumer</strong><span class="zh" lang="zh">个人融资</span>
      </div>
      <div class="service">
        <svg width="36" height="36" viewBox="0 0 36 36" aria-hidden="true">
          <path d="M18,3 L34,18 L30,18 L30,34 L6,34 L6,18 L2,18 Z" fill="var(--red)"/>
          <rect x="14" y="22" width="8" height="12" fill="#fff"/>
        </svg>
        financing<strong>Property</strong><span class="zh" lang="zh">房产融资</span>
      </div>
      <div class="service">
        <svg width="36" height="36" viewBox="0 0 36 36" aria-hidden="true">
          <rect x="2" y="2" width="32" height="32" rx="3" fill="var(--red)"/>
          <rect x="6" y="6" width="24" height="24" fill="#fff"/>
          <rect x="9" y="10" width="8" height="8" fill="var(--red)"/>
          <rect x="19" y="10" width="8" height="2" fill="var(--red)"/>
          <rect x="19" y="14" width="8" height="2" fill="var(--red)"/>
          <rect x="9" y="20" width="18" height="2" fill="var(--red)"/>
          <rect x="9" y="24" width="18" height="2" fill="var(--red)"/>
        </svg>
        financing<strong>business corporate</strong><span class="zh" lang="zh">企业融资</span>
      </div>
    </div>
  </section>
</body>
</html>
```